Zielgruppe
Wir sind eine Imkerei mit angeschlossenem Lehrgarten. Unsere Produktpalette umfasst selbst hergestellte Imkereiprodukte aller Art (Honig, Bienenwachskerzen, Propolis, Pollen, Met). Unsere Zielgruppe sind solvente, umweltbewusste Konsumenten mit dem Sinn für nachhaltig und regional produzierte Waren.
Aufgabenstellung
- Das Etikett soll maximal die Logo-Farben nutzen (weiß, schwarz, gelb), evtl. mit goldenen Akzenten.
- Logo 'Imkerei Fam. Halvers' integrieren
- Ein gleich aussehendes Grundetikett für mehrere Sorten
- Honigname 'Dünenglanz' + Sortenbezeichnung (Rapshonig, Frühtrachthonig, Sommertrachthonig), zusätzlich ein 'Leeretikett' zum Einstempeln von Sondersorten
- Optische Elemente gerne Waben und/oder Regionales (Friesland, Jadebusen, Nordsee)
- Wir erweitern Stück für Stück unser Sortiment, daher soll das Grunddesign später auf Etiketten für zum Beispiel Met, Seife und Bonbons auszuweiten sein.
- Etiketten in 3 verschiedenen Größen nutzbar (500g, 250g, 50g)
- Pflichtangaben auf Honigetiketten: Deutscher Honig/ Honig aus Deutschland, Füllmenge (Schriftgröße mind. 4 mm Höhe), Hersteller/ Name und Anschrift des Imkers (zunächst Platzhalter nutzen, Daten werden im Verlauf übermittelt), Platz für Datumsstempel (MHD), Lagerbedingung (kühl, trocken und dunkel lagern)
- Das Etikett soll einen Gewährverschluss haben, obenauf das leere Feld für den Datumsstempel
- Das Honigglas hat einen goldenen Deep Twist Off Deckel

```html
<!DOCTYPE html>
<html lang="de">
<head>
<meta charset="utf-8">
<title>Dünenglanz – Etikettenserie</title>
<link href="https://fonts.googleapis.com/css2?family=Libre+Baskerville&family=Roboto+Condensed:wght@400;700&display=swap" rel="stylesheet">
<style>
  :root{
    --canvas:#f2f0eb;
    --paper:#ffffff;
    --ink:#3a3632;
    --gold:#d99a1a;
    --comb:#fbecc0;
    --sort-sommer:#e8664a;
    --sort-frueh:#9bbd3c;
    --sort-raps:#ffe400;
    --sort-leer:#c3c0c5;
    --serif:'Libre Baskerville', Georgia, serif;
    --sans:'Roboto Condensed', Arial, sans-serif;
  }
  *{box-sizing:border-box;margin:0;padding:0}
  html,body{width:1200px;height:540px;overflow:hidden;background:var(--canvas)}
  .sheet{position:relative;width:1200px;height:540px}

  /* tamper seal strip */
  .seal{position:absolute;width:69px}
  .seal svg{display:block;width:100%;height:100%}

  .date-disc{position:absolute;left:149px;top:20px;width:144px;height:144px;border-radius:50%;
    border:13px solid var(--sort-sommer);background:var(--paper);
    font-family:var(--sans);font-size:8px;color:var(--ink);text-align:center}
  .date-disc .mhd{position:absolute;top:42px;width:100%}
  .date-disc .stamp-line{position:absolute;left:20px;right:20px;top:66px;border-top:0.8px solid var(--ink)}
  .date-disc .origin{position:absolute;top:82px;width:100%}

  /* label body */
  .label{position:absolute;top:318px;height:156px;background:var(--paper);overflow:hidden}
  .label.unrolled{left:25px;width:390px;top:320px;height:154px;box-shadow:0 0 0 0.6px #ddd}
  .label.front{width:228px}

  .comb{position:absolute;border-radius:4px}
  .comb.a{left:0;top:0;width:120px;height:70px;background:radial-gradient(ellipse at 40% 40%,var(--comb),rgba(251,236,192,0) 70%)}
  .comb.b{right:0;bottom:22px;width:80px;height:70px;background:radial-gradient(ellipse at 60% 60%,var(--comb),rgba(251,236,192,0) 70%)}

  .front-panel{position:absolute;top:0;height:100%;width:228px;text-align:center}
  .unrolled .front-panel{left:82px}
  .front .front-panel{left:0}

  .maker{position:absolute;top:50px;width:100%;font-family:var(--serif);font-size:12px;color:var(--gold);letter-spacing:.3px}
  .maker-ring{position:absolute;left:50%;top:10px;width:96px;height:96px;margin-left:-48px;border-radius:50%;border:0.8px solid var(--ink);opacity:.5}
  .honey-name{position:absolute;top:112px;width:100%;font-family:var(--serif);font-size:18px;letter-spacing:1.2px;color:var(--ink)}

  .sort-band{position:absolute;left:0;right:0;top:141px;height:12px;font-family:var(--sans);font-weight:700;
    font-size:7.5px;letter-spacing:.5px;color:var(--paper);text-align:center;line-height:12px}
  .band-sommer{background:var(--sort-sommer)}
  .band-frueh{background:var(--sort-frueh)}
  .band-raps{background:var(--sort-raps)}
  .band-leer{background:linear-gradient(90deg,var(--sort-leer) 0 34%,var(--paper) 34% 66%,var(--sort-leer) 66%)}

  .side{position:absolute;top:0;font-family:var(--sans);color:var(--ink)}
  .side.left{left:10px;top:42px;width:68px}
  .side.left h3{font-size:5px;font-weight:700;margin-bottom:8px}
  .side.left p{font-size:4.4px;line-height:1.7;text-align:justify}
  .side.right{left:316px;top:42px;width:82px;font-size:4.6px;line-height:1.55}
  .side.right .rule{border-top:0.6px solid var(--ink);margin:3px 0}
  .side.right .weight{font-size:12px;margin-top:4px}
</style>
</head>
<body>
<main class="sheet">

  <!-- Sommertrachthonig: unrolled label with seal and date disc -->
  <div class="date-disc">
    <div class="mhd">Mindestens haltbar bis:</div>
    <div class="stamp-line"></div>
    <div class="origin">Deutscher Honig</div>
  </div>
  <div class="seal" style="left:186px;top:158px;height:163px">
    <svg viewBox="0 0 69 163" preserveAspectRatio="none">
      <rect width="69" height="163" fill="var(--paper)"/>
      <polygon points="0,0 69,0 69,105 0,123" fill="var(--sort-sommer)"/>
    </svg>
  </div>
  <section class="label unrolled">
    <div class="comb a" role="img" aria-label="Wabenmuster in Hellgelb"></div>
    <div class="comb b" role="img" aria-label="Wabenmuster in Hellgelb"></div>
    <div class="side left">
      <h3>DEUTSCHER QUALITÄTSHONIG</h3>
      <p>Lorem ipsum dolor sit amet, consectetuer adipiscing elit, sed diam nonummy nibh eu ismod tincidunt es ut laoreet dolore magna aliquam erat volutpat. Ut wisi enim ad minim veniam, quis nostrud exerci tation ullamcorper suscipit lobortis nisl ut aliquip ex ea commodo con sequat uis autem vel eumes.</p>
    </div>
    <div class="front-panel">
      <div class="maker-ring"></div>
      <div class="maker">Imkerei Fam. Halvers</div>
      <div class="honey-name">DÜNENGLANZ</div>
    </div>
    <div class="side right">
      <div>Trocken, Dunkel und vor Wärme<br>geschützt lagern</div>
      <div class="rule"></div>
      <div>Imkerei Familie Halvers<br>Deichweg 7<br>D-26300 Musterort<br>Tel. 0170-0000000<br>kontakt@imkerei-halvers.de<br>www.imkerei-halvers.de</div>
      <div class="rule"></div>
      <div class="weight">250g</div>
    </div>
    <div class="sort-band band-sommer">SOMMERTRACHTHONIG</div>
  </section>

  <!-- Frühtrachthonig -->
  <div class="seal" style="left:513px;top:227px;height:92px">
    <svg viewBox="0 0 69 92" preserveAspectRatio="none">
      <rect width="69" height="92" fill="var(--paper)"/>
      <polygon points="0,0 69,0 69,32 0,52" fill="var(--sort-frueh)"/>
    </svg>
  </div>
  <section class="label front" style="left:433px">
    <div class="comb a" role="img" aria-label="Wabenmuster in Hellgelb"></div>
    <div class="comb b" role="img" aria-label="Wabenmuster in Hellgelb"></div>
    <div class="front-panel">
      <div class="maker-ring"></div>
      <div class="maker">Imkerei Fam. Halvers</div>
      <div class="honey-name">DÜNENGLANZ</div>
    </div>
    <div class="sort-band band-frueh">FRÜHTRACHTHONIG</div>
  </section>

  <!-- Rapshonig -->
  <div class="seal" style="left:766px;top:227px;height:92px">
    <svg viewBox="0 0 69 92" preserveAspectRatio="none">
      <rect width="69" height="92" fill="var(--paper)"/>
      <polygon points="0,0 69,0 69,32 0,52" fill="var(--sort-raps)"/>
    </svg>
  </div>
  <section class="label front" style="left:686px">
    <div class="comb a" role="img" aria-label="Wabenmuster in Hellgelb"></div>
    <div class="comb b" role="img" aria-label="Wabenmuster in Hellgelb"></div>
    <div class="front-panel">
      <div class="maker-ring"></div>
      <div class="maker">Imkerei Fam. Halvers</div>
      <div class="honey-name">DÜNENGLANZ</div>
    </div>
    <div class="sort-band band-raps">RAPSHONIG</div>
  </section>

  <!-- Leeretikett für Sondersorten -->
  <div class="seal" style="left:1019px;top:227px;height:92px">
    <svg viewBox="0 0 69 92" preserveAspectRatio="none">
      <rect width="69" height="92" fill="var(--paper)"/>
      <polygon points="0,0 69,0 69,32 0,52" fill="var(--sort-leer)"/>
    </svg>
  </div>
  <section class="label front" style="left:939px">
    <div class="comb a" role="img" aria-label="Wabenmuster in Hellgelb"></div>
    <div class="comb b" role="img" aria-label="Wabenmuster in Hellgelb"></div>
    <div class="front-panel">
      <div class="maker-ring"></div>
      <div class="maker">Imkerei Fam. Halvers</div>
      <div class="honey-name">DÜNENGLANZ</div>
    </div>
    <div class="sort-band band-leer"></div>
  </section>

</main>
</body>
</html>
```